We're Hiring Poster or Flyer design

We’re Hiring Details:

Positions include:
Office Manager
Office Assistant
Data Entry Techs
Outreach Manager
Asst. Outreach Manager
Events Coordinator
Drivers (must have personal car, insurance & Driver’s License)
Outreach Specialist—Walkers
Outreach Specialist—Phone/Telemarketing (evenings only)

Excellent Pay ! Fun Atmosphere ! Bonus Pay with Promotional & Career Advancement Opportunities

***************
need 3 formats of SAME flyer:
1) 8.5 x 11
2) 8.5 x 14
3) 11 x17

creative and eye catching a must; this flyer will be used on college bulletin boards and used to attract a younger demographic . . hip and chic look with "Americana style or political motif" preferred.

Target Market(s)

younger demographic . . flyer will be used during college recruiting fairs and in younger settings---age BRACKET is 21 - 35 Years old

Industry/Entity Type

Employment Agency

Font styles to use
Sans Serif

Colors

Designer to choose colors to be used in the design.

Requirements
Must have
• clean and attractive; hip; chic; simple and with good stock pics and layout
Nice to have
• american flag and patriotism
Should not have
• too much details on the job -- I only included the job announcement so you can get an idea of WHAT and WHO I am looking for . . don't list all the BORING details on the flyer/poster

```html
<!DOCTYPE html>
<html lang="en">
<head>
<meta charset="utf-8">
<title>We're Hiring – Marcus Ellery for Mayor</title>
<link href="https://fonts.googleapis.com/css2?family=Oswald:wght@500;600;700&family=Lato:wght@400;700&family=Montserrat:wght@800&display=swap" rel="stylesheet">
<style>
  :root{
    --navy:#0b3472;
    --navy-deep:#072a5c;
    --blue:#1d63a8;
    --orange:#f0621e;
    --red:#e3232b;
    --card:#f3f3f3;
    --ink:#222;
    --ink-soft:#333;
    --page:#e9ecef;
    --white:#fff;
  }
  *{box-sizing:border-box;margin:0;padding:0}
  html,body{width:1200px;height:1200px;overflow:hidden;background:var(--page)}
  .flyer{
    position:absolute;left:151px;top:20px;
    width:842px;height:1088px;background:var(--white);
    transform:scale(1.0662);transform-origin:0 0;
    overflow:hidden;box-shadow:0 4px 18px rgba(0,0,0,.18);
  }
  .hero{position:absolute;left:0;top:0;width:842px;height:434px}
  .hero svg{display:block}
  .campaign-seal{
    position:absolute;left:304px;top:44px;width:232px;height:172px;
    border-radius:50%;background:var(--white);border:4px solid var(--navy);
    display:flex;flex-direction:column;align-items:center;justify-content:center;
    font-family:"Montserrat",sans-serif;font-weight:800;color:var(--navy);
    text-align:center;line-height:1.05;
  }
  .campaign-seal .first{font-size:24px}
  .campaign-seal .last{font-size:34px}
  .headline{position:absolute;left:262px;top:374px;width:300px;height:150px;overflow:visible}
  .headline text{font-family:"Oswald",sans-serif;font-weight:600;fill:var(--white)}
  .positions{
    position:absolute;left:63px;top:523px;width:716px;
    display:grid;grid-template-columns:190px 190px 190px;
    column-gap:64px;row-gap:25px;
  }
  .positions .card{
    height:107px;background:var(--card);
    display:flex;flex-direction:column;align-items:center;justify-content:center;
    font-family:"Lato",sans-serif;font-size:13.5px;color:var(--ink);
    text-align:center;line-height:1.25;padding:0 4px;
  }
  .positions .card:nth-child(3n){transform:translateX(17px)}
  .card svg{width:40px;height:40px;margin-bottom:4px;fill:var(--orange)}
  .card .note{display:block}
  .perks{
    position:absolute;left:0;top:918px;width:842px;text-align:center;line-height:22px;
    font-family:"Oswald",sans-serif;font-weight:600;font-size:19px;letter-spacing:-.2px;
  }
  .perks .pay{color:var(--orange)}
  .perks .fun{color:var(--navy)}
  .bonus{
    position:absolute;left:0;top:942px;width:842px;text-align:center;line-height:22px;
    font-family:Arial,Helvetica,sans-serif;font-size:17.5px;color:var(--ink-soft);
  }
  .call{
    position:absolute;left:0;top:976px;width:842px;height:36px;line-height:36px;
    display:flex;justify-content:center;align-items:center;gap:14px;
    font-family:"Oswald",sans-serif;font-weight:700;font-size:28px;color:var(--navy);
  }
  .call svg{width:30px;height:30px}
  .footer{
    position:absolute;left:0;top:1032px;width:842px;height:56px;background:var(--navy);
    display:flex;align-items:center;justify-content:center;
    font-family:"Lato",sans-serif;font-weight:700;font-size:13px;letter-spacing:3px;color:var(--white);
  }
</style>
</head>
<body>
<svg width="0" height="0" style="position:absolute" aria-hidden="true">
  <defs>
    <symbol id="ico-person" viewBox="0 0 44 44">
      <circle cx="22" cy="12" r="8"/>
      <path d="M4 42c0-10 7-17 18-17s18 7 18 17z"/>
      <path d="M22 25l-2.5 5 2.5 10 2.5-10z" fill="#fff"/>
    </symbol>
    <symbol id="ico-laptop" viewBox="0 0 44 44">
      <circle cx="22" cy="9" r="7"/>
      <path d="M8 36c0-9 6-15 14-15s14 6 14 15z"/>
      <rect x="11" y="26" width="22" height="12" rx="1" fill="#fff"/>
      <rect x="13" y="28" width="18" height="8"/>
      <rect x="7" y="38" width="30" height="3"/>
    </symbol>
    <symbol id="ico-calendar" viewBox="0 0 44 44">
      <rect x="6" y="9" width="32" height="29" rx="2"/>
      <rect x="12" y="5" width="3" height="8"/><rect x="29" y="5" width="3" height="8"/>
      <g fill="#fff">
        <rect x="10" y="18" width="5" height="4"/><rect x="17" y="18" width="5" height="4"/><rect x="24" y="18" width="5" height="4"/><rect x="31" y="18" width="4" height="4"/>
        <rect x="10" y="25" width="5" height="4"/><rect x="17" y="25" width="5" height="4"/><rect x="24" y="25" width="5" height="4"/><rect x="31" y="25" width="4" height="4"/>
        <rect x="10" y="31" width="5" height="4"/><rect x="17" y="31" width="5" height="4"/>
      </g>
    </symbol>
    <symbol id="ico-driver" viewBox="0 0 44 44">
      <circle cx="22" cy="10" r="8"/>
      <path d="M6 40c0-10 7-16 16-16s16 6 16 16z"/>
      <circle cx="22" cy="34" r="9" fill="none" stroke="#fff" stroke-width="3"/>
      <rect x="13" y="33" width="18" height="3" fill="#fff"/>
    </symbol>
    <symbol id="ico-gear" viewBox="0 0 44 44">
      <circle cx="22" cy="12" r="7"/>
      <g fill="#fff"><circle cx="22" cy="12" r="3"/></g>
      <g><rect x="20.5" y="2" width="3" height="4"/><rect x="20.5" y="18" width="3" height="4"/><rect x="12" y="10.5" width="4" height="3"/><rect x="28" y="10.5" width="4" height="3"/></g>
      <path d="M6 42c0-9 7-16 16-16s16 7 16 16z"/>
      <path d="M22 26l-2.5 5 2.5 10 2.5-10z" fill="#fff"/>
    </symbol>
    <symbol id="ico-phone-gear" viewBox="0 0 44 44">
      <circle cx="15" cy="16" r="7"/>
      <path d="M2 42c0-9 6-15 13-15s13 6 13 15z"/>
      <path d="M15 27l-2 4 2 10 2-10z" fill="#fff"/>
      <circle cx="33" cy="10" r="8" fill="none" stroke="currentColor" stroke-width="2.5"/>
      <circle cx="33" cy="10" r="3"/>
    </symbol>
  </defs>
</svg>

<main class="flyer">
  <section class="hero">
    <svg width="842" height="434" viewBox="0 0 842 434">
      <defs>
        <linearGradient id="flag-tone" x1="0" y1="0" x2="1" y2="0">
          <stop offset="0" stop-color="#c9cde6"/>
          <stop offset=".45" stop-color="#eef0f8"/>
          <stop offset=".7" stop-color="#f6c9c4"/>
          <stop offset="1" stop-color="#e98f86"/>
        </linearGradient>
        <linearGradient id="sky-tone" x1="0" y1="0" x2="1" y2="1">
          <stop offset="0" stop-color="#0f3a7e"/>
          <stop offset="1" stop-color="#1e6db3"/>
        </linearGradient>
        <linearGradient id="crowd-tone" x1="0" y1="0" x2="0" y2="1">
          <stop offset="0" stop-color="#2a3550" stop-opacity=".55"/>
          <stop offset="1" stop-color="#3a3f4d" stop-opacity=".8"/>
        </linearGradient>
      </defs>
      <rect width="842" height="220" fill="url(#flag-tone)" role="img" aria-label="Waving American flag photograph"/>
      <path d="M0 200 Q421 70 842 190 L842 434 L0 434 Z" fill="url(#sky-tone)"/>
      <path d="M0 220 Q421 80 842 210" fill="none" stroke="var(--red)" stroke-width="9"/>
      <path d="M0 242 Q421 102 842 232" fill="none" stroke="var(--red)" stroke-width="5"/>
      <path d="M0 200 Q421 70 842 190" fill="none" stroke="var(--navy)" stroke-width="14"/>
      <rect x="96" y="186" width="640" height="248" rx="40" fill="url(#crowd-tone)" role="img" aria-label="Photograph of five smiling young adults holding notebooks and backpacks"/>
      <line x1="0" y1="433" x2="842" y2="433" stroke="var(--navy)" stroke-width="2"/>
    </svg>
    <div class="campaign-seal">
      <span class="first">Marcus</span>
      <span class="last">Ellery</span>
    </div>
  </section>

  <svg class="headline" viewBox="0 0 300 150" aria-label="We're Hiring">
    <path d="M5 7 L117 5 L119 85 L72 85 L44 100 L50 85 L7 86 Z" fill="var(--orange)"/>
    <text x="21" y="55" font-size="46" textLength="80" lengthAdjust="spacingAndGlyphs">WE’RE</text>
    <path d="M102 9 L294 6 L290 139 L190 140 L156 152 L160 141 L104 143 Z" fill="var(--navy)"/>
    <text x="120" y="103" font-size="84" textLength="156" lengthAdjust="spacingAndGlyphs">HIRING</text>
  </svg>

  <section class="positions">
    <div class="card"><svg><use href="#ico-person"/></svg>Office Manager</div>
    <div class="card"><svg><use href="#ico-person"/></svg>Office Assistant</div>
    <div class="card"><svg><use href="#ico-laptop"/></svg>Data Entry Techs</div>
    <div class="card"><svg><use href="#ico-person"/></svg>Outreach Manager</div>
    <div class="card"><svg><use href="#ico-person"/></svg>Asst. Outreach Manager</div>
    <div class="card"><svg><use href="#ico-calendar"/></svg>Events Coordinator</div>
    <div class="card"><svg><use href="#ico-driver"/></svg>Drivers<span class="note">(must have personal car,<br>insurance &amp; Driver’s License)</span></div>
    <div class="card"><svg><use href="#ico-gear"/></svg>Outreach Specialist<br>—Walkers</div>
    <div class="card"><svg style="color:var(--orange)"><use href="#ico-phone-gear"/></svg>Outreach Specialist<br>—Phone/Telemarketing<br>(evenings only)</div>
  </section>

  <p class="perks"><span class="pay">EXCELLENT PAY !</span> <span class="fun">FUN ATMOSPHERE !</span></p>
  <p class="bonus">Bonus Pay with Promotional &amp; Career Advancement Opportunities</p>
  <p class="call">
    <span>CALL US NOW</span>
    <svg viewBox="0 0 30 30" aria-hidden="true">
      <path d="M8 3l4 6-3 3c1.5 3.5 4.5 6.5 8 8l3-3 6 4-2 5c-10 0-21-11-21-21z" fill="none" stroke="var(--orange)" stroke-width="2.4" stroke-linejoin="round"/>
      <path d="M18 4a9 9 0 0 1 8 8M18 9a4 4 0 0 1 3 3" fill="none" stroke="var(--orange)" stroke-width="2"/>
    </svg>
    <span>555-210-487</span>
  </p>
  <footer class="footer">www.ElleryForMayor.com</footer>
</main>
</body>
</html>
```